Thank you for exploring whether you are interested in creating a book cover for The Insight Lantern!

The cover should look professional yet appeal to a person who is open to approaching life more deeply.

The logo that I've uploaded is something that you are welcome to use in your book cover design but is not required to be the primary graphic.

The following is a description of The Insight Lantern and its purpose.
RADICAL CLARITY IS POSSIBLE

Are you tired of hitting up against your limitations? Do you wish you could be more effective in everything you do? What would it be like if you could walk confidently into any situation and automatically comprehend it, organize your thoughts, and respond creatively? This kind of radical clarity is not only possible, it’s right in front of you—and The Insight Lantern: Notice Every Signal. Hold Bold Dialogues. Build the Path You Choose. shows you the pathway to get there!

In the book, Dr. Gavin Terlecki draws on over 30 years of experience with executive coaching and leadership development to deliver priceless wisdom about how to see clearly in today’s complex and uncertain world. Using his Insight Lantern, you’ll discover where you’re stuck and why, find your authentic direction, and learn to engage creatively with life so you can start getting what you really want.

A TRANSFORMATIONAL TOOL

The Insight Lantern is a cutting-edge leadership development tool that supports you to activate your maximum potential, both personally and professionally. It’s based on the idea that there are four fundamental building blocks to reality: Intentions, Actions, Facts, and Stories. Understanding the differences between these dimensions of your experience and learning how they work together is the key to forging a clear path toward your destination in life. The Insight Lantern organizes these four main building blocks around the two polarities of a compass:

1. North to South – Intentions to Actions
We all have billions of intentions, but how many do we actually put into action? In this polarity you learn to notice and implement your intentions in order to generate more effective actions and create meaningful outcomes in your life.

2. East vs. West – Facts vs. Stories
We all create stories to make sense of life, but how many of us actually get clear on the facts to see where our stories might be off? In this polarity you learn to discern the objective facts from your subjective interpretations and stories, illuminating a clearer perspective to uncover what’s been blocking you on the path to success.

Using The Insight Lantern you’ll discover how naming and implementing your intentions in life naturally results in more effective behavior and actions, and how distinguishing the real facts from your interpretations of any situation can propel you toward radical clarity and true fulfillment.

BOLD DIALOGUES

The key benefit of using The Insight Lantern is that you’ll have more of what Gavin calls “Bold Dialogues.” Bold Dialogues are those that move you closer to what you’re wanting in life—the kind of human-to-human interactions that actually make a difference. By applying The Insight Lantern, you gain critical insight that opens your eyes to new opportunities for Bold Dialogues, helping you draw on your imagination and move beyond your current stance toward a positive outcome. Every conversation is a possibility waiting to be discovered. The more Bold Dialogues you have, the more profound and meaningful shifts you activate in your life.

PRACTICAL GUIDANCE

The book doesn’t just give you a theoretical understanding of how to gain more clarity in your life. Dr. Terlecki provides you with clear, practical steps to develop the core competencies you need to start getting the results you want. As you explore the book, you’ll find:

• A thorough description of all the directions of The Insight Lantern, each with three main points to focus your energy on.
• Case studies from Gavin’s many clients who have successfully used The Insight Lantern to transform their own lives.
• Hands-on practices Gavin has developed to help you put your new skills to use immediately.
• Step-by-step guidance to apply The Insight Lantern in any situation, including real-life stories from people who have experienced genuine transformation using this tool.

The Insight Lantern will help you to deepen your understanding of the challenges in your life, integrate new competencies to boost your effectiveness, and awaken to exciting opportunities for your own growth, leadership, and success!

ABOUT THE AUTHOR

Dr. Gavin Terlecki has over 30 years of experience with leadership development and executive coaching work. As owner and principal coach of Terlecki Growth Advisors, he has been integrating the fields of management consulting, business psychology, and leadership coaching since 1983. Gavin holds a Ph.D. in psychodynamic and group psychology from the Halvern Graduate Academy, an M.A. in human growth and potential from the Marlowe Ridge University, and a B.A. in accounting and Business Administration from Denby Valley University. He is the creator of The Insight Lantern™, a leadership development tool that supports people to see life clearly, wake up to exciting opportunities for their own growth and leadership, and take empowered action toward true success. Gavin’s combination of business expertise, human compassion, and incisive questions help his clients achieve unprecedented results.

Target Market(s)

Out intended audience is folks who would like to be more effective and to grow and transform. This being more productive and developing could be in their careers or their personal lives.

Industry/Entity Type

It Professional

Requirements
Must have
• Stock images, if used, that I can purchase exclusively or that you can easily create specifically for the book once you are the chosen designer. I completely understand using stock imaging in your submissions pre-selection.
Nice to have
• Ideally the cover will include both the title and subtitle.

```html
<!DOCTYPE html>
<html lang="en">
<head>
<meta charset="utf-8">
<title>The Insight Lantern – Book Cover</title>
<link rel="stylesheet" href="https://fonts.googleapis.com/css2?family=Nunito+Sans:ital,wght@0,300;0,400;0,600;0,700;1,400&display=swap">
<style>
  :root {
    --stage: #e9e7e2;
    --cover: #000000;
    --blue-deep: #1274c4;
    --blue-bright: #29a9e1;
    --blue-line: #1d5f9c;
    --text-soft: #b9b9b9;
    --text-white: #f2f2f2;
    --frame: #3a4a78;
    --emblem-a: #29a9e1;
    --emblem-b: #0d3f66;
  }
  * { box-sizing: border-box; margin: 0; padding: 0; }
  html, body {
    width: 1200px; height: 1000px; overflow: hidden;
    background: var(--stage);
    font-family: "Nunito Sans", Arial, sans-serif;
  }
  .jacket {
    position: absolute; left: 75px; top: 130px;
    display: flex; height: 740px;
  }
  /* Back cover */
  .back-cover {
    width: 490px; height: 100%; background: var(--cover);
    padding: 40px 34px 0; color: var(--text-soft); position: relative;
  }
  .back-heading {
    font-size: 12px; letter-spacing: 1.5px; color: var(--text-soft); font-weight: 400;
    padding-bottom: 10px; border-bottom: 1px solid var(--blue-line);
  }
  .praise { margin-top: 16px; font-size: 11.5px; line-height: 1.55; }
  .praise + .praise { margin-top: 12px; }
  .praise-source {
    text-align: center; font-style: italic; color: var(--blue-bright);
    font-size: 11px; line-height: 1.25; padding-left: 150px;
  }
  .author-bio { margin-top: 20px; font-size: 11.5px; line-height: 1.6; }
  .author-photo {
    float: left; width: 60px; height: 80px; margin: 2px 8px 2px 0;
    background: linear-gradient(160deg, #ffffff, #c9cfe0);
    border: 2px solid var(--frame);
  }
  .author-bio strong { color: #8ea3cf; font-weight: 600; }
  .feature-row {
    margin-top: 22px; display: flex; align-items: flex-start;
    justify-content: space-between;
  }
  .feature-note {
    width: 145px; font-size: 10.5px; line-height: 1.6; color: var(--text-white);
    padding: 6px 0 6px 26px; border-left: 1px solid var(--blue-line);
  }
  .feature-note.right { border-left: none; border-right: 1px solid var(--blue-line); padding: 6px 26px 6px 0; }
  .brand-mark { text-align: center; width: 120px; }
  .brand-dot {
    width: 60px; height: 60px; border-radius: 50%; margin: 0 auto 8px;
    border: 3px solid var(--text-white);
  }
  .brand-name { font-size: 10.5px; line-height: 1.2; color: var(--blue-bright); }
  .back-rule {
    position: absolute; left: 34px; right: 34px; bottom: 102px;
    border-top: 1px solid var(--frame);
  }
  .back-boxes {
    position: absolute; left: 34px; right: 34px; bottom: 26px;
    display: flex; justify-content: space-between;
  }
  .back-box {
    width: 108px; height: 56px; border: 1.5px solid var(--frame);
    display: flex; align-items: center; justify-content: center;
    font-size: 11px; letter-spacing: 1.5px; color: #8b8b9a;
  }
  /* Spine */
  .spine {
    width: 70px; height: 100%; background: var(--cover);
    border-left: 1px solid #222; border-right: 1px solid #222;
    display: flex; flex-direction: column; justify-content: space-between;
    align-items: center; padding: 40px 0;
  }
  .spine-text {
    writing-mode: vertical-rl; font-size: 17px; letter-spacing: 1.5px;
    color: var(--blue-bright); font-weight: 400;
  }
  .spine-text.title { color: var(--blue-deep); }
  /* Front cover */
  .front-cover {
    width: 490px; height: 100%; background: var(--cover);
    padding: 40px 36px 0; text-align: center; position: relative;
  }
  .front-author {
    font-size: 22px; letter-spacing: 3px; color: var(--text-white);
    font-weight: 400; padding-bottom: 10px; border-bottom: 1.5px solid var(--blue-line);
  }
  .front-title { margin-top: 10px; font-weight: 300; line-height: 0.98; }
  .front-title .line-one { display: block; font-size: 60px; color: var(--blue-deep); }
  .front-title .line-two { display: block; font-size: 76px; color: var(--blue-bright); letter-spacing: 1px; }
  .front-emblem {
    width: 330px; height: 330px; margin: 22px auto 0; border-radius: 50%;
    background: radial-gradient(circle at 50% 50%, var(--emblem-a) 0%, #1f8fcc 45%, var(--emblem-b) 100%);
  }
  .front-tagline {
    margin-top: 34px; font-size: 21px; letter-spacing: 3.5px; line-height: 1.55;
    color: var(--text-white); font-weight: 400;
  }
</style>
</head>
<body>
  <main class="jacket">
    <section class="back-cover">
      <h2 class="back-heading">LOREM IPSUM</h2>

      <blockquote class="praise">
        <p>“Lorem ipsum greeking and more of the same this is praise for Dr. Terlecki’s new book lorem ipsum greeeking and you will see more clearly lorem ipsum.”</p>
        <p class="praise-source">- &nbsp;Marcus Delaney<br>Director of Lorem Isum Center</p>
      </blockquote>
      <blockquote class="praise">
        <p>“Lorem ipsum greeking and more of the same this is praise for Dr. Terlecki’s new book lorem ipsum greeeking and you will see more clearly lorem ipsum.”</p>
        <p class="praise-source">- &nbsp;Rosalind Whitcombe<br>Director of Lorem Isum Center</p>
      </blockquote>

      <p class="author-bio">
        <span class="author-photo" role="img" aria-label="Author portrait photo"></span>
        <strong>Dr. Gavin Terlecki</strong> and more of the same this is praise for Dr. Terlecki’s new book lorem ipsum greeeking and you will see more clearly loremipsum . Lorem ipsum greeking and more of the same this is praise for Dr. Terlecki’s new book lorem ipsum greeeking and you will see more clearly lorem ipsum and more to see. Lorem ipsum greeking and more of the same this is praise for Dr. Terlecki’s new book lorem ipsum greeeking and you will see more clearly lorem ipsum plus newlor. Lorem ipsum greeking and more of the same this is praise for Dr. Terlecki’s new book lorem ipsum greeeking and you will see more clearly lorem ipsum .
      </p>

      <div class="feature-row">
        <p class="feature-note">Lorem ipsum greeking more of the same lorem greeking ipsum</p>
        <div class="brand-mark">
          <div class="brand-dot"></div>
          <p class="brand-name">THE INSIGHT<br>LANTERN</p>
        </div>
        <p class="feature-note right">Lorem ipsum greeking more of the same lorem greeking ipsum</p>
      </div>

      <div class="back-rule"></div>
      <div class="back-boxes">
        <div class="back-box">PUBLISHER</div>
        <div class="back-box">UPC CODE</div>
      </div>
    </section>

    <aside class="spine">
      <span class="spine-text title">THE INSIGHT LANTERN</span>
      <span class="spine-text">DR. GAVIN TERLECKI</span>
    </aside>

    <section class="front-cover">
      <p class="front-author">DR. GAVIN TERLECKI</p>
      <h1 class="front-title">
        <span class="line-one">THE INSIGHT</span>
        <span class="line-two">LANTERN</span>
      </h1>
      <div class="front-emblem" role="img" aria-label="Large blue cover emblem for The Insight Lantern"></div>
      <p class="front-tagline">NOTICE EVERY SIGNAL.<br>HOLD BOLD DIALOGUES.<br>BUILD THE PATH YOU CHOOSE.</p>
    </section>
  </main>
</body>
</html>
```